Silver Bloom Marisol's Cleaning Service Business Cards Project

A business card with all contact details with logo design on there (already have a logo) eye catching Logo and contact info on one side, full logo on the back, must target upper class residential and corporate companies, fitness companies, still keep it on the feminine side of things , must look elegant

Target Market(s)

Upper class homes and corporate companies

Industry/Entity Type

Cleaning Service

Contact Information for Business Card

Name: Marisol Venturo
Position: Director
ABN: 47193802564
Email: marisolssilvercleaning@fernmail.test
Number: 0417968341

Font styles to use
Decorative

Colors

Designer to choose colors to be used in the design.

Requirements
Must have
• Available Sydney Wide, contact info and logo on one side, full logo on the back
Nice to have
• Professional appearance
Should not have
• Cheap advert looking stuff

```html
<!DOCTYPE html>
<html lang="en">
<head>
<meta charset="utf-8">
<title>Silver Bloom – Business Cards</title>
<link rel="stylesheet" href="https://fonts.googleapis.com/css2?family=Lora:wght@500&family=Open+Sans:wght@400&family=Oswald:wght@500&display=swap">
<style>
  :root {
    --backdrop: #e9e6e2;
    --card: #2c313d;
    --accent: #5fcfcb;
    --ink-light: #f2f4f6;
    --rule: #d9dde2;
  }
  * { margin: 0; padding: 0; box-sizing: border-box; }
  html, body {
    width: 1200px; height: 1000px; overflow: hidden;
    background: var(--backdrop);
  }
  .canvas { position: relative; width: 1200px; height: 1000px; }
  .card {
    position: absolute; left: 267px; width: 665px; height: 396px;
    background: var(--card); border-radius: 26px;
  }
  .card--front { top: 75px; }
  .card--back { top: 535px; }

  .brand-mark {
    position: absolute; left: 302px; top: 120px;
    width: 62px; height: 62px; border: 2px solid var(--accent); border-radius: 50%;
  }
  .brand-name {
    position: absolute; left: 0; right: 0; top: 262px; text-align: center;
    font-family: "Lora", serif; font-weight: 500; font-size: 37px;
    letter-spacing: 1px; color: var(--accent); text-transform: uppercase;
  }
  .brand-tagline {
    position: absolute; left: 0; right: 0; top: 313px; text-align: center;
    font-family: "Open Sans", sans-serif; font-size: 13.5px;
    letter-spacing: 3.2px; color: var(--ink-light); text-transform: uppercase;
  }

  .person {
    position: absolute; right: 416px; top: 168px; text-align: right;
  }
  .person__name {
    font-family: "Oswald", sans-serif; font-weight: 500; font-size: 24px;
    line-height: 1.1; color: var(--accent); text-transform: uppercase;
  }
  .person__role {
    font-family: "Open Sans", sans-serif; font-size: 15px; color: var(--ink-light);
    margin-top: 3px;
  }
  .divider {
    position: absolute; left: 269px; top: 167px; width: 1.5px; height: 56px;
    background: var(--rule);
  }
  .contacts {
    position: absolute; left: 285px; top: 163px; list-style: none;
    font-family: "Open Sans", sans-serif; font-size: 15px; line-height: 21.5px;
    color: var(--ink-light);
  }
  .contacts li { display: flex; align-items: center; gap: 6px; }
  .contacts svg { width: 14px; height: 14px; flex: none; }
</style>
</head>
<body>
<main class="canvas">
  <section class="card card--front">
    <span class="brand-mark" aria-hidden="true"></span>
    <h1 class="brand-name">Silver Bloom</h1>
    <p class="brand-tagline">Marisol’s Cleaning Service</p>
  </section>

  <section class="card card--back">
    <div class="person">
      <h2 class="person__name">Marisol Venturo</h2>
      <p class="person__role">Director</p>
    </div>
    <span class="divider" aria-hidden="true"></span>
    <ul class="contacts">
      <li>ABN: 47193802564</li>
      <li>
        <svg viewBox="0 0 24 24" fill="none" stroke="#5fcfcb" stroke-width="1.8" aria-hidden="true"><path d="M5 3h4l2 5-2.5 1.5a11 11 0 0 0 6 6L16 13l5 2v4a2 2 0 0 1-2 2A16 16 0 0 1 3 5a2 2 0 0 1 2-2z"/></svg>
        0417968341
      </li>
      <li>
        <svg viewBox="0 0 24 24" fill="none" stroke="#5fcfcb" stroke-width="1.8" aria-hidden="true"><rect x="3" y="5" width="18" height="14" rx="1"/><path d="M3 6l9 7 9-7"/></svg>
        marisolssilvercleaning@fernmail.test
      </li>
    </ul>
  </section>
</main>
</body>
</html>
```